Lorvenna vineyards

Wine label/logo that is old world witH a modern Maybe Latin/Hispanic twist. Nothing cartoonish or colorful.
Updates

This is a wine vineyard growing tempranillo, Malbec, cabarnet. I am looking for a wine label that incorporates the logo for Lorvenna Vineyards. Location Temecula california

```html
<!DOCTYPE html>
<html lang="en">
<head>
<meta charset="utf-8">
<title>Lorvenna Vineyards – Wine Labels</title>
<link rel="stylesheet" href="https://fonts.googleapis.com/css2?family=Montserrat:wght@500;600&family=Source+Serif+4:ital,opsz,wght@0,8..60,700;1,8..60,400&display=swap">
<style>
  :root {
    --backdrop: #b8b8b8;
    --ink: #231f20;
    --wine-red: #ed1c24;
    --paper: #ffffff;
  }
  * { margin: 0; padding: 0; box-sizing: border-box; }
  html, body {
    width: 1200px;
    height: 1200px;
    overflow: hidden;
    background: var(--backdrop);
  }
  .label-row {
    position: relative;
    width: 1200px;
    height: 1200px;
  }
  .label {
    position: absolute;
    top: 459px;
    width: 370px;
    height: 282px;
    text-align: center;
  }
  .label--tempranillo { left: 32px; top: 458px; background: var(--ink); color: var(--paper); }
  .label--cabernet { left: 415px; background: var(--wine-red); color: var(--paper); }
  .label--malbec { left: 799px; background: var(--paper); color: var(--ink); }

  .brand-name {
    position: absolute;
    left: 0; right: 0;
    top: 124px;
    font-family: "Montserrat", sans-serif;
    font-weight: 600;
    font-size: 23px;
    letter-spacing: 0.52em;
    padding-left: 0.52em;
    line-height: 1;
  }
  .brand-sub {
    position: absolute;
    left: 0; right: 0;
    top: 169px;
    font-family: "Montserrat", sans-serif;
    font-weight: 500;
    font-size: 9px;
    letter-spacing: 0.42em;
    padding-left: 0.42em;
    line-height: 1;
  }
  .varietal {
    position: absolute;
    left: 0; right: 0;
    top: 231px;
    font-family: "Source Serif 4", serif;
    font-weight: 700;
    font-size: 16px;
    line-height: 1;
  }
  .origin {
    position: absolute;
    left: 0; right: 0;
    top: 253px;
    font-family: "Source Serif 4", serif;
    font-style: italic;
    font-size: 7.5px;
    line-height: 1;
  }
</style>
</head>
<body>
<main class="label-row">
  <section class="label label--tempranillo">
    <p class="brand-name">LORVENNA</p>
    <p class="brand-sub">VINEYARDS</p>
    <p class="varietal">tempranillo 2018</p>
    <p class="origin">temecula . california</p>
  </section>
  <section class="label label--cabernet">
    <p class="brand-name">LORVENNA</p>
    <p class="brand-sub">VINEYARDS</p>
    <p class="varietal">cabernet</p>
    <p class="origin">temecula . california</p>
  </section>
  <section class="label label--malbec">
    <p class="brand-name">LORVENNA</p>
    <p class="brand-sub">VINEYARDS</p>
    <p class="varietal">malbec</p>
    <p class="origin">temecula . california</p>
  </section>
</main>
</body>
</html>
```